Tall ridge firewood

It a new firewood outlet in Ridgemoor Vale that will only sell top hardwood firewood (ironbark , red gum, grey gum, an box mix. I would like to see a web page the we can do order online payment for delivery. It will all so need to have photos of the firewood. I all so have logo for tall ridge firewood
Must have a modem look but easy to use I would like to see a black back ground of some sort.

Here are some other firewood web pages for ideas and firewood info
http://www.kestrelfirewood.example.au
http://www.dunmorefirewood.example.au
http://www.wrenlogfirewood.example.au
http://www.tallisbluelogs.example.au/firewood

```html
<!DOCTYPE html>
<html lang="en">
<head>
<meta charset="utf-8">
<title>Tall Ridge Firewood</title>
<link href="https://fonts.googleapis.com/css2?family=Roboto+Condensed:wght@400;700&family=Arimo:wght@400;700&display=swap" rel="stylesheet">
<style>
:root{
  --blue:#1b72c0;
  --blue-nav:#2e8ddf;
  --blue-light:#3192e3;
  --dark:#1f1f1f;
  --text:#6b6b6b;
  --text-dark:#333;
  --tile:#f1f1f1;
  --footer:#efefef;
  --rule:#dcdcdc;
  --white:#fff;
}
*{box-sizing:border-box;margin:0;padding:0}
html,body{width:1038px;height:1200px;overflow:hidden}
body{position:relative;background:var(--white);font-family:"Arimo",Arial,sans-serif;color:var(--text)}
.backdrop{position:absolute;left:0;top:0;width:1038px;height:558px;background:linear-gradient(90deg,#0e0e0e,#1d1d1d 40%,#161616 60%,#0d0d0d)}
.page-head{position:absolute;left:139px;top:0;width:760px;height:176px;background:var(--blue)}
.brand{position:absolute;left:19px;top:0;width:186px;height:157px;background:var(--white);display:flex;flex-direction:column;align-items:center;justify-content:center;gap:10px}
.brand-mark{width:70px;height:70px;border-radius:50%;background:var(--blue)}
.brand-name{font-family:"Roboto Condensed",sans-serif;font-weight:700;font-size:15px;color:var(--blue);letter-spacing:.2px}
.call{position:absolute;left:375px;top:62px;color:var(--white)}
.call small{display:block;font-size:11px;color:#cfe3f6}
.call strong{display:block;font-size:19px;font-weight:700;margin-top:3px}
.address{position:absolute;left:559px;top:62px;color:var(--white);font-size:10.5px;line-height:13px}
.address a{color:var(--white)}
.address span{color:#cfe3f6}
.nav{position:absolute;left:139px;top:176px;width:760px;height:30px;background:var(--blue-nav);display:flex;padding-left:19px}
.nav a{font-family:"Roboto Condensed",sans-serif;font-size:11.5px;color:var(--white);text-decoration:none;display:flex;align-items:center;justify-content:center;border-right:1px solid #4ea0e8;text-transform:uppercase}
.nav a.active{background:var(--dark);border-right:none}
.nav a:last-child{border-right:none}
.hero{position:absolute;left:139px;top:206px;width:760px;height:352px;background:radial-gradient(ellipse 32% 46% at 62% 55%,#ffd35a 0%,#f08a1e 30%,#8a3a10 60%,transparent 75%),linear-gradient(90deg,#4a3a2e,#6a5140 30%,#3a2b20 70%,#241c16)}
.hero-caption{position:absolute;left:246px;top:160px;width:269px;height:33px;background:var(--blue);border:1px solid var(--white);color:var(--white);font-size:17px;display:flex;align-items:center;justify-content:center;letter-spacing:.2px}
.hero-caption b{margin:0 5px}
.arrow{position:absolute;top:164px;width:30px;height:24px;background:var(--white);display:flex;align-items:center;justify-content:center}
.arrow.prev{left:0}
.arrow.next{right:0}
.products{position:absolute;left:139px;top:583px;width:760px;display:flex;gap:46px}
.product{width:156px}
.product .photo{height:118px}
.product .label{height:43px;background:var(--tile);display:flex;align-items:center;justify-content:center;font-family:"Roboto Condensed",sans-serif;font-size:15px;color:var(--text-dark);text-transform:uppercase}
.product.current .label{background:var(--blue);color:var(--white)}
.col{position:absolute;top:792px;height:186px}
.col h2{font-family:"Roboto Condensed",sans-serif;font-weight:400;font-size:19.5px;color:var(--blue);text-transform:uppercase;margin-top:3px}
.col p{font-size:10px;line-height:12px}
.welcome{left:139px;width:200px}
.welcome p{margin-top:18px}
.welcome p+p{margin-top:12px}
.why{left:420px;width:220px}
.news{left:690px;width:210px}
.divider{position:absolute;top:792px;width:1px;height:186px;background:var(--rule)}
.list{list-style:none;margin-top:18px}
.list li{display:flex;gap:9px;height:38px}
.list .num{font-family:"Roboto Condensed",sans-serif;font-weight:700;font-size:19px;color:var(--text-dark);width:22px;line-height:20px}
.btn{position:absolute;top:958px;height:21px;padding:0 12px;background:linear-gradient(#3a3a3a,#111);color:var(--white);font-size:9.5px;display:flex;align-items:center;text-transform:uppercase}
.footer{position:absolute;left:0;top:1012px;width:1038px;height:160px;background:var(--footer);border-bottom:1px solid var(--rule)}
.fcol{position:absolute;top:24px}
.fcol h3{font-size:9.5px;font-weight:700;color:var(--blue);text-transform:uppercase}
.fcol ul{list-style:none;margin-top:8px}
.fcol li{font-size:9px;color:#555;height:13.6px}
.fcol li::before{content:"»";margin-right:6px;color:#777}
.cards{display:flex;gap:8px;margin-top:10px}
.cards span{width:31px;height:19px;background:#fff;border:1px solid #ccc}
.social{display:flex;gap:4px;margin-top:9px}
.social span{width:23px;height:23px;background:var(--blue)}
.happy h3{font-size:13.5px;text-transform:none}
.happy p{font-size:9.5px;line-height:12px;color:#555;margin-top:7px;width:250px}
.happy .who{margin-top:10px}
.happy .btn{position:static;display:inline-flex;margin-top:12px;background:var(--blue-light);height:20px}
.copyright{position:absolute;left:0;top:1180px;width:1038px;text-align:center;font-size:9px;color:#777;text-transform:uppercase}
</style>
</head>
<body>
<div class="backdrop"></div>

<header class="page-head">
  <div class="brand">
    <span class="brand-mark"></span>
    <span class="brand-name">TALL RIDGE FIREWOOD</span>
  </div>
  <div class="call"><small>Call us</small><strong>0455 019 372</strong></div>
  <div class="address">215, Lorem Ipsum is simply dummy<br>Ridgemoor Vale<br><span>Email - </span><a href="#">info@tallridgefirewood.example.au</a></div>
</header>

<nav class="nav">
  <a class="active" href="#" style="width:80px">Home</a>
  <a href="#" style="width:85px">About Us</a>
  <a href="#" style="width:91px">Products</a>
  <a href="#" style="width:109px">Order Online</a>
  <a href="#" style="width:106px">Accessories</a>
  <a href="#" style="width:83px">Delivery</a>
  <a href="#" style="width:69px">Faq`s</a>
  <a href="#" style="width:102px">Contact Us</a>
</nav>

<section class="hero" role="img" aria-label="Photo of hardwood logs burning in a stone fireplace">
  <div class="arrow prev"><svg width="10" height="14" viewBox="0 0 10 14"><path d="M8 1 2 7l6 6" fill="none" stroke="#1b72c0" stroke-width="3"/></svg></div>
  <div class="hero-caption">TOP <b>HARDWOOD</b> FIREWOOD</div>
  <div class="arrow next"><svg width="10" height="14" viewBox="0 0 10 14"><path d="M2 1l6 6-6 6" fill="none" stroke="#1b72c0" stroke-width="3"/></svg></div>
</section>

<section class="products">
  <div class="product current"><div class="photo" role="img" aria-label="Photo of split ironbark firewood" style="background:linear-gradient(135deg,#3a1e0c,#9a5a2a 50%,#2a160a)"></div><div class="label">Ironbark</div></div>
  <div class="product"><div class="photo" role="img" aria-label="Photo of stacked red gum firewood" style="background:linear-gradient(135deg,#b98a78,#8e5a48 50%,#c9a090)"></div><div class="label">Red Gum</div></div>
  <div class="product"><div class="photo" role="img" aria-label="Photo of a pile of grey gum logs" style="background:linear-gradient(135deg,#8d8a80,#5f5c55 50%,#a29e94)"></div><div class="label">Grey Gum</div></div>
  <div class="product"><div class="photo" role="img" aria-label="Photo of box mix firewood burning in a grate" style="background:radial-gradient(ellipse 40% 50% at 50% 45%,#ffb13a,#c2501a 45%,#2a1a12 80%)"></div><div class="label">Box Mix</div></div>
</section>

<section class="col welcome">
  <h2>Welcome to our site</h2>
  <p>Lorem ipsum dolor sit amet, consectetur adipisicing elit, sed do eiusmod tempor incididunt ut labore et dolore magna aliqua. Ut enim ad minim veniam, quis nostrud exercitation ullamco.</p>
  <p>Duis aute irure dolor in reprehenderit in voluptate velit esse cillum dolore eu fugiat nulla pariatur ...</p>
</section>
<a class="btn" style="left:139px">Read More</a>
<div class="divider" style="left:378px"></div>

<section class="col why">
  <h2>Why choose us?</h2>
  <ul class="list">
    <li><svg width="12" height="12" viewBox="0 0 12 12"><path d="M1 6l3 3 7-7" fill="none" stroke="#999" stroke-width="2"/></svg><p>Lorem ipsum dolor sit amet, consectetur adipisicing elit.</p></li>
    <li><svg width="12" height="12" viewBox="0 0 12 12"><path d="M1 6l3 3 7-7" fill="none" stroke="#999" stroke-width="2"/></svg><p>Lorem ipsum dolor sit amet, consectetur adipisicing elit.</p></li>
    <li><svg width="12" height="12" viewBox="0 0 12 12"><path d="M1 6l3 3 7-7" fill="none" stroke="#999" stroke-width="2"/></svg><p>Lorem ipsum dolor sit amet, consectetur adipisicing elit.</p></li>
  </ul>
</section>
<a class="btn" style="left:420px">Read More</a>
<div class="divider" style="left:655px"></div>

<section class="col news">
  <h2>Latest News</h2>
  <ul class="list">
    <li><span class="num">01</span><p>Lorem ipsum dolor sit amet, consectetur adipisicing elit.</p></li>
    <li><span class="num">02</span><p>Lorem ipsum dolor sit amet, consectetur adipisicing elit.</p></li>
    <li><span class="num">03</span><p>Lorem ipsum dolor sit amet, consectetur adipisicing elit.</p></li>
  </ul>
</section>
<a class="btn" style="left:690px">View All</a>

<footer class="footer">
  <div class="fcol" style="left:140px">
    <h3>Navigation</h3>
    <ul><li>Home</li><li>About Us</li><li>Products</li><li>Accessories</li><li>Contact Us</li></ul>
  </div>
  <div class="fcol" style="left:284px">
    <h3>Order Online</h3>
    <ul><li>Terms &amp; Conditions</li><li>Delivery</li><li>Faq`s</li></ul>
  </div>
  <div class="fcol" style="left:454px">
    <h3>Payment Option</h3>
    <div class="cards"><span></span><span></span><span></span></div>
    <h3 style="margin-top:22px">Follow us on</h3>
    <div class="social"><span></span><span></span><span></span><span></span></div>
  </div>
  <div class="fcol happy" style="left:654px;top:20px">
    <h3>Happy Client`s</h3>
    <p>Lorem ipsum dolor sit amet, consectetur adipisicing elit, sed do eiusmod tempor incididunt ut labore et dolore magna aliqua.</p>
    <p class="who"><b>Mara</b>. 15/06/13</p>
    <a class="btn">Read More</a>
  </div>
</footer>
<div class="copyright">Copyright © Tall Ridge Firewood 2013. All right reserved.</div>
</body>
</html>
```